" Trabalhei muitos anos em escritórios de Arquitetura, Construtoras, Escritórios de projetos para grandes Magazines, tive uma sociedade onde fiz obras e projetos de decoração, mas agora finalmente estou criando a Movera para trabalhar como autônoma. Vou juntar toda minha experiência nesses anos e aplicar na realização dos sonhos dos clientes. "

```html
<!DOCTYPE html>
<html lang="pt-BR">
<head>
<meta charset="utf-8">
<title>Movera Arquitetura – Cartão de visita</title>
<link rel="stylesheet" href="https://fonts.googleapis.com/css2?family=Montserrat:wght@300;400;500;600&display=swap">
<style>
  :root {
    --page-bg: #f2f1ef;
    --card-grey: #8b8783;
    --copper: #e0ab8f;
    --ink-light: #ffffff;
    --ink-soft: #ecebea;
    --card-shadow: rgba(0, 0, 0, 0.18);
  }
  * { box-sizing: border-box; margin: 0; padding: 0; }
  html, body {
    width: 1200px; height: 1200px; overflow: hidden;
    background: var(--page-bg);
    font-family: "Montserrat", sans-serif;
  }
  .sheet {
    width: 1200px; height: 1200px;
    display: flex; flex-direction: column; align-items: center; justify-content: center;
    gap: 60px;
  }
  .card {
    width: 840px; height: 480px;
    background: var(--card-grey);
    box-shadow: 0 10px 30px var(--card-shadow);
    position: relative;
  }
  .card--back { display: flex; align-items: center; justify-content: center; }
  .card--back .brand-name { font-size: 64px; }
  .brand-name {
    font-weight: 500;
    color: var(--copper);
    letter-spacing: 0.08em;
    text-transform: uppercase;
  }
  .card--front .brand-block {
    position: absolute; left: 60px; top: 150px; width: 300px; height: 110px;
    display: flex; align-items: center; justify-content: center;
  }
  .card--front .brand-name { font-size: 56px; }
  .contact-block {
    position: absolute; left: 400px; top: 88px; right: 40px;
    color: var(--ink-light);
  }
  .person-name {
    font-size: 30px; font-weight: 500; letter-spacing: 0.02em; text-transform: uppercase;
  }
  .person-role {
    font-size: 14px; font-weight: 400; letter-spacing: 0.22em; text-transform: uppercase;
    color: var(--ink-soft); margin: 2px 0 22px 2px;
  }
  .contact-list { list-style: none; }
  .contact-item {
    display: flex; align-items: center; gap: 12px;
    font-size: 20px; font-weight: 400; margin-bottom: 10px;
    white-space: nowrap;
  }
  .contact-icon { width: 24px; height: 24px; flex: none; }
  .location {
    position: absolute; left: 60px; bottom: 44px;
    font-size: 18px; font-weight: 300; letter-spacing: 0.42em;
    color: var(--ink-soft); text-transform: uppercase;
    white-space: nowrap;
  }
</style>
</head>
<body>
<main class="sheet">
  <section class="card card--back" aria-label="Verso do cartão">
    <span class="brand-name">Movera</span>
  </section>

  <section class="card card--front" aria-label="Frente do cartão">
    <div class="brand-block">
      <span class="brand-name">Movera</span>
    </div>

    <div class="contact-block">
      <h1 class="person-name">Helena Bastos</h1>
      <p class="person-role">Arquiteta</p>
      <ul class="contact-list">
        <li class="contact-item">
          <svg class="contact-icon" viewBox="0 0 24 24" aria-hidden="true">
            <circle cx="12" cy="12" r="10.5" fill="none" stroke="#fff" stroke-width="1.5"/>
            <path d="M8.5 7.5c.6-.6 1.3-.5 1.6 0l1 1.6c.3.5.2 1-.2 1.3l-.6.5c.5 1.2 1.5 2.2 2.7 2.8l.5-.6c.3-.4.9-.5 1.3-.2l1.6 1c.5.3.6 1 0 1.6-1 1-2.4 1.1-4.6-.5-1.6-1.2-2.7-2.5-3.4-4-.8-1.7-.6-2.8.1-3.5z" fill="#fff"/>
          </svg>
          <span>(31) 99512-4470</span>
        </li>
        <li class="contact-item">
          <svg class="contact-icon" viewBox="0 0 24 24" aria-hidden="true">
            <circle cx="12" cy="12" r="10.5" fill="none" stroke="#fff" stroke-width="1.5"/>
            <path d="M8.5 7.5c.6-.6 1.3-.5 1.6 0l1 1.6c.3.5.2 1-.2 1.3l-.6.5c.5 1.2 1.5 2.2 2.7 2.8l.5-.6c.3-.4.9-.5 1.3-.2l1.6 1c.5.3.6 1 0 1.6-1 1-2.4 1.1-4.6-.5-1.6-1.2-2.7-2.5-3.4-4-.8-1.7-.6-2.8.1-3.5z" fill="#fff"/>
          </svg>
          <span>(31) 99512-4470</span>
        </li>
        <li class="contact-item">
          <svg class="contact-icon" viewBox="0 0 24 24" aria-hidden="true">
            <circle cx="12" cy="12" r="10.5" fill="none" stroke="#fff" stroke-width="1.5"/>
            <rect x="6.5" y="8" width="11" height="8" fill="none" stroke="#fff" stroke-width="1.4"/>
            <path d="M6.5 8l5.5 4.5L17.5 8" fill="none" stroke="#fff" stroke-width="1.4"/>
          </svg>
          <span>contato@movera-arq.com.br</span>
        </li>
        <li class="contact-item">
          <svg class="contact-icon" viewBox="0 0 24 24" aria-hidden="true">
            <circle cx="12" cy="12" r="10.5" fill="none" stroke="#fff" stroke-width="1.5"/>
          </svg>
          <span>@movera.arquitetura</span>
        </li>
      </ul>
    </div>

    <p class="location">Vale Serrano - MG | Brasil</p>
  </section>
</main>
</body>
</html>
```